Driftwood Dales Restaurant Web Design

Driftwood Dales Grill and Bar

https://driftwooddales.example
Logo available on existing website.

Images Availble at Social Media
www.facebook.com/driftwooddales/
www.instagram.com/driftwooddales/

Driftwood Dales is a full service Restaurant and bar on Pelican Shoal Key, FL. They are highlited by excellent food in a casual Island sports atmosphere. They are frequented by Locals and Tourist Alike. We would like to push the quality of their food which includes a large menu variety, a late night full liqour bar with sports and TVs, and a convenient location at the front of the Island. They have very good reviews from google and FB.

1. Header and Footer Template
A. Header Template
1. Logo
2. Social Icons | Phone # and Icon | Address | Reviews Icon
3. Main Menu - With Dropdowns
a.Menus - Dinner, Lunch, Drinks - Liqour, Wine, Beer, Specials
b.About us - About us, Local Links, Disclaimer, Privacy policy, Accessability
c.Blog/ Calendar/Events
d. Contact Us
B. Footer Template -
1. Static Banner with Logo links to DD Liqour, 7128, mvt liqour
1. Duplicate Above Info - Different Layout
2. Socket with Copyright etc.

2. Front Page
A. Hero Section - Image Slider? h1 Tag + Description
B. Food Menu Images and Links Section
C. Daily Specials Post (single Post Layout - MENU CPT - Daily Special Category)
D. Testimonials Slider -Include link to more reviews (google, Trip Advisor etc.)
E. Blog / Events 3 column Post Section.
A static Banner Ad needs to be at the bottom linking to Driftwood Spirits and Coffee shop

3. Inernal Pages
A. Blog Template Page for Events/Blog - If we go with a calendar plugin this will deviate.

B. Menu CPT - food-menu - set your slug / rewrite url: restaurant-pelican-shoal-key
1. Each Menu will need a page template to display menu items. Lunch/Dinner/Specials/Drinks (liqour,Beer,Wine )

C. Contact Us Page - No Form - Google Map - Location address phone.
D. About Us Page - Static Page - Images and content to Highlight Quality of Food. Late Night Bar - Sports Bar

E. Static Pages - Accessabily Page, Privacy Policy, DisclaimerRestaurant Website Redesign.

Industry/Entity Type

Restaraunt

Number of Pages Required

5+ page

Requirements
Nice to have
• Please give us some unique restaurant designs. not a standard template

```html
<!DOCTYPE html>
<html lang="en">
<head>
<meta charset="utf-8">
<title>Contact – Driftwood Spirits</title>
<link href="https://fonts.googleapis.com/css2?family=Inter:wght@400;500;600;700&family=Oswald:wght@500;700&display=swap" rel="stylesheet">
<style>
:root{
  --ink:#111;
  --blue:#2f4a8f;
  --grey:#666;
  --light:#e8e8e8;
  --footer:#161616;
  --footer-text:#9a9a9a;
  --white:#fff;
}
*{box-sizing:border-box;margin:0;padding:0}
html,body{width:720px;height:1200px;overflow:hidden;background:var(--white);font-family:"Inter",sans-serif;color:var(--ink)}
.page{position:relative;width:720px;height:1200px}
.abs{position:absolute}
.topbar{left:0;top:0;width:720px;height:27px;background:#000;color:#fff;font-size:6.5px;font-weight:500}
.topbar .item{position:absolute;top:9px;display:flex;align-items:center;gap:5px}
.topbar .sep{position:absolute;top:7px;width:1px;height:13px;background:#444}
.header{left:0;top:27px;width:720px;height:49px;background:#fff}
.brand{position:absolute;left:89px;top:17px;font-family:"Oswald",sans-serif;font-weight:500;font-size:10px;letter-spacing:2.4px;color:#2b2418}
.nav{position:absolute;top:23px;font-size:7.4px;font-weight:500}
.nav.active{color:var(--blue)}
.nav.active::after{content:"";position:absolute;left:1px;right:1px;top:12px;height:1px;background:var(--blue)}
.call{left:546px;top:40px;width:22px;height:22px;border-radius:50%;background:var(--blue)}
.call-label{left:575px;top:42px;font-size:6px}
.call-num{left:575px;top:51px;font-family:"Oswald",sans-serif;font-weight:500;font-size:8.5px}
.hero{left:0;top:76px;width:720px;height:165px;background:linear-gradient(120deg,#6f7e8e 0%,#4a1a1c 25%,#8c8e90 50%,#4e1b1f 72%,#b08a6a 100%)}
.hero-shade{left:0;top:76px;width:720px;height:165px;background:rgba(0,0,0,.25)}
.pill{left:322px;top:142px;width:78px;height:13px;background:var(--blue);border-radius:2px;color:#fff;font-size:7px;text-align:center;line-height:13px}
.hero-title{left:0;width:720px;top:162px;text-align:center;font-family:"Oswald",sans-serif;font-weight:700;font-size:17px;color:#fff}
.side-tab{left:691px;top:182px;width:29px;height:106px;background:#fff;border-radius:14px 0 0 14px}
.side-dot{width:15px;height:15px;border-radius:50%;background:#eceef3;left:698px}
.help-title{left:0;width:720px;top:264px;text-align:center;font-family:"Oswald",sans-serif;font-weight:700;font-size:18px}
.help-text{left:0;width:720px;top:296px;text-align:center;font-size:7.3px;line-height:16px}
.ring{width:44px;height:44px;border-radius:50%;border:1px solid var(--blue);left:88px}
.ring::after{content:"";position:absolute;inset:2px;border-radius:50%;border:1px solid #c9d1e6}
.ring svg{position:absolute;left:12px;top:12px}
.link-line{left:110px;width:1px;background:#b8c2dc}
.info-title{left:148px;font-size:8px;font-weight:700}
.info-text{left:148px;font-size:7px;color:var(--grey);line-height:14px}
.photo{background:linear-gradient(160deg,#6c8aa2,#3f5568)}
.map{left:0;top:684px;width:720px;height:278px;background:linear-gradient(135deg,#e2e2e2,#d6d6d6 60%,#cfcfcf)}
.map-card{left:12px;top:693px;width:178px;height:69px;background:#fff;box-shadow:0 1px 3px rgba(0,0,0,.2)}
.footer{left:0;top:962px;width:720px;height:238px;background:var(--footer)}
.f-head{font-family:"Oswald",sans-serif;font-weight:500;font-size:9px;color:#fff;top:1009px}
.f-bar{top:1011px;width:2px;height:9px;background:var(--blue)}
.f-text{font-size:7px;color:var(--footer-text);line-height:14px}
.f-div{top:1009px;width:1px;height:85px;background:#2c2c2c}
.f-dot{top:1106px;width:16px;height:16px;border-radius:50%;background:#262626}
</style>
</head>
<body>
<div class="page">

  <div class="abs topbar">
    <div class="item" style="left:91px"><svg width="7" height="9" viewBox="0 0 7 9"><path d="M3.5 0a3.3 3.3 0 0 0-3.3 3.3C.2 5.8 3.5 9 3.5 9s3.3-3.2 3.3-5.7A3.3 3.3 0 0 0 3.5 0z" fill="#fff"/><circle cx="3.5" cy="3.3" r="1.2" fill="#000"/></svg>4820 Shoreline Ave, Pelican Shoal Key, FL 34990</div>
    <div class="sep" style="left:248px"></div>
    <div class="item" style="left:278px"><svg width="10" height="9"><rect x="0.5" y="3" width="9" height="5.5" fill="none" stroke="#fff"/><path d="M1 1h8" stroke="#fff"/></svg>Kitchen Hours: 11.30AM - 9PM&nbsp; Sun To Thurs.&nbsp; Fri, Sat - 10pm</div>
    <div class="sep" style="left:499px"></div>
    <div class="item" style="left:528px"><svg width="11" height="10"><rect x="1" y="2" width="3" height="7" fill="none" stroke="#fff"/><rect x="6" y="5" width="4" height="4" fill="none" stroke="#fff"/></svg>Bar Open To 12AM 7 Days</div>
  </div>

  <div class="abs header">
    <div class="brand">DRIFTWOOD SPIRITS</div>
    <div class="nav active" style="left:259px">HOME</div>
    <div class="nav" style="left:297px">MENUS</div>
    <div class="nav" style="left:338px">ABOUT US</div>
    <div class="nav" style="left:389px">BLOG</div>
    <div class="nav" style="left:427px">CONTACT US</div>
  </div>
  <div class="abs call"><svg width="22" height="22" viewBox="0 0 22 22"><path d="M8 7c1 3 3 6 7 8l1.5-1.5 1.5 1-1 2c-5 0-10-5-10-10l2-1 1 1.5z" fill="none" stroke="#fff" stroke-width="1"/></svg></div>
  <div class="abs call-label">Call Now</div>
  <div class="abs call-num">+1 555-014-2290</div>

  <div class="abs hero" role="img" aria-label="Photo of two glasses of red wine on a dining table with salad and bread"></div>
  <div class="abs hero-shade"></div>
  <div class="abs pill">Get In Touch</div>
  <div class="abs hero-title">CONTACT</div>
  <div class="abs side-tab"></div>
  <div class="abs side-dot" style="top:196px"></div>
  <div class="abs side-dot" style="top:218px"></div>
  <div class="abs side-dot" style="top:242px"></div>
  <div class="abs side-dot" style="top:264px"></div>

  <div class="abs help-title">HERE TO HELP!...</div>
  <div class="abs help-text">Have a question about the our service? We're here<br>to help, contact us today!.</div>

  <div class="abs link-line" style="top:402px;height:34px"></div>
  <div class="abs link-line" style="top:483px;height:37px"></div>
  <div class="abs link-line" style="top:565px;height:38px"></div>

  <div class="abs ring" style="top:357px"><svg width="20" height="20" viewBox="0 0 20 20"><path d="M10 2a5 5 0 0 0-5 5c0 4 5 9 5 9s5-5 5-9a5 5 0 0 0-5-5z" fill="none" stroke="#2f4a8f"/><circle cx="10" cy="7" r="2" fill="none" stroke="#2f4a8f"/><path d="M4 16c2 2 10 2 12 0" fill="none" stroke="#2f4a8f"/></svg></div>
  <div class="abs ring" style="top:438px"><svg width="20" height="20" viewBox="0 0 20 20"><path d="M5 3c1 5 5 10 11 12l1-3-3-1-1.5 1.5C10 11 8 9 7 7l1.5-1.5-1-3z" fill="none" stroke="#2f4a8f"/><path d="M12 3a5 5 0 0 1 5 5M12 6a2 2 0 0 1 2 2" fill="none" stroke="#2f4a8f"/></svg></div>
  <div class="abs ring" style="top:520px"><svg width="20" height="20" viewBox="0 0 20 20"><rect x="1" y="2" width="8" height="6" fill="none" stroke="#2f4a8f"/><rect x="1" y="11" width="18" height="7" fill="none" stroke="#2f4a8f"/><path d="M12 8h6M15 3v5" stroke="#2f4a8f"/></svg></div>
  <div class="abs ring" style="top:604px"><svg width="20" height="20" viewBox="0 0 20 20"><rect x="2" y="8" width="16" height="10" fill="none" stroke="#2f4a8f"/><path d="M4 8V3h12v5M5 14h10" fill="none" stroke="#2f4a8f"/></svg></div>

  <div class="abs info-title" style="top:359px">LOCATION</div>
  <div class="abs info-text" style="top:374px">123, Restaurant St, Food City,<br>Newyork 04.</div>
  <div class="abs info-title" style="top:440px">GENERAL QUERIES</div>
  <div class="abs info-text" style="top:455px">800-12345-67-879<br>supportyou@example.com</div>
  <div class="abs info-title" style="top:522px">KITCHEN HOURS</div>
  <div class="abs info-text" style="top:537px">Sun to Thurs 11.30AM - 9PM<br>Fri, Sat - 10pmPM</div>
  <div class="abs info-title" style="top:613px">BAR WORKING HOURS</div>
  <div class="abs info-text" style="top:628px">All Day 12 PM</div>

  <div class="abs photo" style="left:292px;top:356px;width:191px;height:241px" role="img" aria-label="Photo of croissants, blood oranges and coffee on a dark board over a blue surface"></div>
  <div class="abs" style="left:523px;top:370px;width:82px;height:82px;border-radius:50%;border:1px solid #dde2ee"></div>
  <div class="abs" style="left:532px;top:379px;width:64px;height:64px;border-radius:50%;background:radial-gradient(circle,#6b5a3c,#3a2e22)" role="img" aria-label="Photo of mushroom and avocado toast"></div>
  <div class="abs" style="left:501px;top:464px;width:130px;height:170px;background:linear-gradient(170deg,#6e6e6e,#2d2d2d 60%,#1f1f1f)" role="img" aria-label="Photo of crusted skewers in a black bowl with dipping sauces"></div>

  <div class="abs map" role="img" aria-label="Road map showing the restaurant location"></div>
  <div class="abs" style="left:374px;top:812px;width:16px;height:22px"><svg width="16" height="22" viewBox="0 0 16 22"><path d="M8 0a8 8 0 0 0-8 8c0 6 8 14 8 14s8-8 8-14a8 8 0 0 0-8-8z" fill="#555"/><circle cx="8" cy="8" r="3" fill="#333"/></svg></div>
  <div class="abs map-card">
    <div class="abs" style="left:13px;top:9px;font-size:7.5px;font-weight:700">DRIFTWOOD SPIRITS</div>
    <div class="abs" style="left:13px;top:24px;font-size:6px;line-height:10px;color:#444">123, Restaurant St, Food City,<br>Newyork 04.</div>
    <div class="abs" style="left:13px;top:52px;font-size:6px;color:#444">View Larger Map</div>
    <div class="abs" style="left:137px;top:8px;width:12px;height:12px"><svg width="12" height="12"><path d="M2 11V6l6-4M5 2h3v3" fill="none" stroke="#777" stroke-width="1.5"/></svg></div>
    <div class="abs" style="left:137px;top:23px;font-size:5.5px;color:#555">Directions</div>
  </div>

  <div class="abs footer"></div>
  <div class="abs f-bar" style="left:88px"></div>
  <div class="abs f-head" style="left:96px">CONTACT DETAILS</div>
  <div class="abs" style="left:88px;top:1044px"><svg width="12" height="14" viewBox="0 0 12 14"><path d="M6 1a4.5 4.5 0 0 0-4.5 4.5C1.5 9 6 13 6 13s4.5-4 4.5-7.5A4.5 4.5 0 0 0 6 1z" fill="none" stroke="#9a9a9a"/><circle cx="6" cy="5.5" r="1.5" fill="none" stroke="#9a9a9a"/></svg></div>
  <div class="abs f-text" style="left:114px;top:1036px">4820 Shoreline Ave, Pelican Shoal Key,<br>FL 34990</div>
  <div class="abs" style="left:88px;top:1076px"><svg width="12" height="12" viewBox="0 0 12 12"><path d="M2 1c.5 4 4 8 9 9l.5-2-2-1-1 1C6.5 7 5 5.5 4.5 4l1-1-1-2z" fill="none" stroke="#9a9a9a"/></svg></div>
  <div class="abs f-text" style="left:112px;top:1075px">+1 555-014-2290</div>
  <div class="abs f-dot" style="left:88px"></div>
  <div class="abs f-dot" style="left:111px"></div>
  <div class="abs f-dot" style="left:135px"></div>
  <div class="abs f-dot" style="left:158px"></div>
  <div class="abs f-div" style="left:254px"></div>
  <div class="abs f-div" style="left:461px"></div>

  <div class="abs" style="left:0;width:720px;top:1003px;text-align:center;font-family:'Oswald',sans-serif;font-weight:500;font-size:12px;letter-spacing:3px;color:#fff">DRIFTWOOD SPIRITS</div>
  <div class="abs f-text" style="left:270px;width:180px;top:1048px;text-align:center">The way they make shows is, they make one show. That show's called a pilot. Then they show that show to the people who make shows.</div>
  <div class="abs" style="left:311px;top:1101px;width:98px;height:23px;border:1px solid var(--blue);color:#9aa6c4;font-size:7.3px;text-align:center;line-height:21px">NO RESERVATION</div>

  <div class="abs f-bar" style="left:499px"></div>
  <div class="abs f-head" style="left:506px">WORKING HOURS</div>
  <div class="abs" style="left:500px;top:1040px"><svg width="14" height="14"><rect x="0.5" y="5" width="13" height="8" fill="none" stroke="#9a9a9a"/><path d="M1 2h12M4 9h6" stroke="#9a9a9a"/></svg></div>
  <div class="abs f-text" style="left:527px;top:1038px"><span style="color:#bbb;font-weight:600">Kitchen Hours:</span><br>11.30AM - 9PM&nbsp; Sun To Thurs.<br>Fri, Sat - 10pm</div>
  <div class="abs" style="left:502px;top:1088px"><svg width="14" height="18"><rect x="1" y="5" width="5" height="12" fill="none" stroke="#9a9a9a"/><rect x="8" y="9" width="5" height="5" fill="none" stroke="#9a9a9a"/></svg></div>
  <div class="abs f-text" style="left:527px;top:1086px"><span style="color:#bbb;font-weight:600">Bar Open :</span><br><span style="font-size:6.3px">12 PM 7 Days</span></div>

  <div class="abs" style="left:0;width:720px;top:1161px;text-align:center;font-size:5px;color:#4a4a4a">Copyright © 2016 DRIFTWOOD DALES. All rights reserved.</div>
</div>
</body>
</html>
```